Corvid Lens Studio Business Card Design

I need a business card designed for a photography business based in Perth, Western Australia called Corvid Lens Studio.

We specialise in wedding, event photography and portrait photography.

The business card must borrow the style of the attached logo.

The hex codes for the colours in the logo are:
#ED1D85 - Pink
#89C23E - Green
#37282F - Black

The name on the card will be:
Name: Tobiah
Phone: 0417395268
Website: www.corvidlensstudio.com.au
Facebook: corvidlensstudio

I am open and happy to accept creative concepts.

Industry/Entity Type

Business

```html
<!DOCTYPE html>
<html lang="en">
<head>
<meta charset="UTF-8">
<title>Corvid Lens Studio – Business Card</title>
<link rel="stylesheet" href="https://fonts.googleapis.com/css2?family=Cinzel:wght@400&family=Crimson+Text:wght@400&display=swap">
<style>
  :root {
    --pink: #ED1D85;
    --green: #89C23E;
    --ink: #37282F;
    --cream: #F1EBD6;
    --backdrop: #3A3A3C;
  }
  * { margin: 0; padding: 0; box-sizing: border-box; }
  html, body {
    width: 1200px; height: 900px; overflow: hidden;
    background: var(--backdrop);
  }
  .canvas {
    position: relative; width: 1200px; height: 900px;
    display: flex; flex-direction: column; align-items: center; justify-content: center; gap: 24px;
  }
  .card {
    position: relative; width: 700px; height: 400px;
    background: var(--cream);
    overflow: hidden;
  }
  .rule { position: absolute; height: 1.5px; }
  .rule--pink { background: var(--pink); }
  .rule--green { background: var(--green); }

  /* Front */
  .front-mark {
    position: absolute; left: 50%; top: 62px; width: 76px; height: 76px;
    margin-left: -38px; border-radius: 50%;
    border: 2px solid var(--pink);
  }
  .front-title {
    position: absolute; left: 0; right: 0; top: 196px; text-align: center;
    font-family: "Cinzel", serif; font-size: 22px; letter-spacing: 0.55em;
    color: var(--ink); padding-left: 0.55em;
  }
  .front-location {
    position: absolute; left: 0; right: 0; top: 236px; text-align: center;
    font-family: "Crimson Text", serif; font-size: 14px; letter-spacing: 0.08em;
    color: var(--ink);
  }

  /* Back */
  .back-name {
    position: absolute; left: 0; right: 0; top: 100px; text-align: center;
    font-family: "Cinzel", serif; font-size: 72px; letter-spacing: 0.04em;
    color: var(--ink);
  }
  .contact {
    position: absolute; display: flex; align-items: center; gap: 8px;
    font-family: "Crimson Text", serif; font-size: 19px; color: var(--ink);
  }
  .contact-icon {
    width: 22px; height: 22px; border-radius: 4px; background: var(--pink);
    display: flex; align-items: center; justify-content: center; flex: none;
  }
  .contact-row { position: absolute; right: 36px; top: 228px; display: flex; gap: 22px; }
  .contact-row .contact { position: static; }
  .contact--web { left: 36px; top: 336px; }
</style>
</head>
<body>
<main class="canvas">
  <section class="card card--front" aria-label="Card front">
    <div class="front-mark"></div>
    <div class="rule rule--pink" style="left:330px; right:0; top:186px;"></div>
    <h1 class="front-title">CORVID LENS STUDIO</h1>
    <p class="front-location">Perth, Western Australia</p>
    <div class="rule rule--green" style="left:0; width:380px; top:268px;"></div>
  </section>

  <section class="card card--back" aria-label="Card back">
    <h2 class="back-name">TOBIAH</h2>
    <div class="contact-row">
      <span class="contact">
        <span class="contact-icon">
          <svg width="14" height="14" viewBox="0 0 24 24" aria-hidden="true"><path fill="#fff" d="M6.6 10.8a15.1 15.1 0 0 0 6.6 6.6l2.2-2.2a1 1 0 0 1 1-.25 11.4 11.4 0 0 0 3.6.57 1 1 0 0 1 1 1V20a1 1 0 0 1-1 1A17 17 0 0 1 3 4a1 1 0 0 1 1-1h3.5a1 1 0 0 1 1 1c0 1.25.2 2.45.57 3.57a1 1 0 0 1-.25 1z"/></svg>
        </span>
        0417395268
      </span>
      <span class="contact">
        <span class="contact-icon"></span>
        corvidlensstudio
      </span>
    </div>
    <div class="rule rule--pink" style="left:330px; right:0; top:272px;"></div>
    <div class="rule rule--green" style="left:0; width:380px; top:318px;"></div>
    <span class="contact contact--web">
      <span class="contact-icon">
        <svg width="14" height="14" viewBox="0 0 24 24" aria-hidden="true" fill="none" stroke="#fff" stroke-width="1.8"><circle cx="12" cy="12" r="9"/><ellipse cx="12" cy="12" rx="4" ry="9"/><path d="M3 12h18"/></svg>
      </span>
      www.corvidlensstudio.com.au
    </span>
  </section>
</main>
</body>
</html>
```